Emergency Management Consulting Needs a Website

Need to develop a website for an Emergency Management Consulting business. This website needs to be user friendly and resemble disaster preparedness, response, recovery, and mitigation. It must allow for me to make changes to it myself by adding pages, content and pictures. Looking for an advanced page to the website that allows monitoring of social media sites, hashtags, and keywords. Must have pictures of disasters on the site. Must try to integrate the logo colors, not excessive.

Reason: Did not receive anything sufficient to what I am looking for.

Industry/Entity Type

Government

Coding

Coded - Design and coding required

Number of Pages Required

5+ page

Requirements
Must have
• Logo, advanced social media monitoring page, allow for edits myself (content, pages, graphics) this must be a CMS of some sort, use logo color scheme (not excessively), must be professional looking, connect with Vexlo Domain, find a hosting site, SEO, no "long" designs, minimize "dead" space, no social media feeds, no newsletter stuff.
• Menu items: Home, About Us, Services, Situation Monitor, Work With Us, Contact Us (hopefully these could be editable if I need to later)
• When you make a submission, please send me a message on which CMS you are using. Thank you.
Nice to have
• Examples of websites:
• https://www.plorn.vic.gov.au/
• http://www.garvelmunds.com/
• http://www.tqplaxr.org/
• http://dumbrellconsulting.com/
• http://www.folvantix.com/services/emergency-management
• https://qzu.com/
• http://www.belmorvia.com/Responsibility/Sustainable-Development/HSE/Crisis-and-Emergency-Management/

```html
<!DOCTYPE html>
<html lang="en">
<head>
<meta charset="utf-8">
<title>Kelvara Response Group</title>
<link rel="stylesheet" href="https://fonts.googleapis.com/css2?family=Montserrat:wght@200;300;400;500;600;700;800&display=swap">
<style>
:root{
  --red:#e2302f;
  --red-deep:#c9262a;
  --ink:#111111;
  --dark:#2b2b2b;
  --grey:#777777;
  --white:#ffffff;
  --nav:#222222;
}
*{margin:0;padding:0;box-sizing:border-box}
html,body{width:1200px;height:1128px;overflow:hidden;background:var(--white)}
body{font-family:'Montserrat',sans-serif;position:relative}
.site-header{position:absolute;left:0;top:0;width:1200px;height:61px;background:var(--white)}
.brand{position:absolute;left:136px;top:12px;display:flex;align-items:center;gap:7px}
.brand-mark{width:22px;height:22px;border-radius:50%;background:var(--red)}
.brand-name{font-weight:700;font-size:15px;color:var(--dark);letter-spacing:.3px;line-height:1}
.main-nav a{position:absolute;top:17px;font-size:12.5px;color:var(--nav);text-decoration:none;letter-spacing:.6px;font-weight:400}
.hero{position:absolute;left:0;top:61px;width:1200px;height:498px;overflow:hidden}
.hero-photo{position:absolute;inset:0;background:linear-gradient(120deg,#8a7f78 0%,#6d6058 35%,#5a4e47 60%,#7f6d63 100%)}
.hero-shapes{position:absolute;inset:0}
.hero-copy{position:absolute;left:133px;top:0;color:var(--white)}
.hero-lead{position:absolute;top:76px;left:0;white-space:nowrap;font-weight:200;font-size:43px;letter-spacing:-.5px}
.hero-title{position:absolute;top:134px;left:0;white-space:nowrap;font-weight:800;font-size:52px;line-height:66px;letter-spacing:-1.5px}
.hero-text{position:absolute;top:278px;left:0;width:370px;font-size:12.5px;line-height:14.5px;font-weight:500}
.btn-more{position:absolute;top:365px;left:5px;width:161px;height:42px;border-radius:21px;background:var(--dark);color:var(--white);font-weight:700;font-size:16px;display:flex;align-items:center;justify-content:center;text-decoration:none}
.help{position:absolute;left:0;top:559px;width:1200px;height:515px}
.help-heading{position:absolute;top:70px;left:0;width:1200px;text-align:center;font-weight:800;font-size:34px;letter-spacing:-1px;color:var(--ink)}
.help-heading span{color:var(--red)}
.help-card{position:absolute;top:144px;width:300px;text-align:center}
.help-photo{width:165px;height:165px;margin:0 auto;border-radius:50%;border:8px solid var(--white);box-shadow:0 0 4px rgba(0,0,0,.18)}
.help-title{margin-top:22px;font-weight:600;font-size:22px;letter-spacing:1.3px;color:var(--ink)}
.help-text{margin-top:12px;font-size:12.5px;line-height:14.5px;color:var(--grey);padding:0 18px}
.band{position:absolute;left:0;top:1074px;width:1200px;height:54px}
.band-photo{position:absolute;left:0;top:0;width:630px;height:54px;background:linear-gradient(90deg,#3a3f34,#262b22 50%,#3b3a30)}
.band-panel{position:absolute;left:630px;top:0;width:570px;height:54px;background:var(--red)}
</style>
</head>
<body>
<header class="site-header">
  <div class="brand"><span class="brand-mark"></span><span class="brand-name">KELVARA RESPONSE</span></div>
  <nav class="main-nav">
    <a href="#" style="left:451px">Home</a>
    <a href="#" style="left:527px">About Us</a>
    <a href="#" style="left:624px">Services</a>
    <a href="#" style="left:714px">Situation Monitor</a>
    <a href="#" style="left:866px">Work With Us</a>
    <a href="#" style="left:990px">Contact Us</a>
  </nav>
</header>

<section class="hero">
  <div class="hero-photo" role="img" aria-label="Responder in a vest standing among debris of destroyed houses after a disaster"></div>
  <svg class="hero-shapes" width="1200" height="498" viewBox="0 0 1200 498">
    <polygon points="0,0 666,0 414,498 0,498" fill="#e2302f"/>
    <polygon points="414,498 480,367 552,498" fill="#3a3a3a"/>
  </svg>
  <div class="hero-copy">
    <div class="hero-lead">AT-THE-READY TO PROVIDE</div>
    <h1 class="hero-title">IMMEDIATE DISASTER<br>CASE MANAGEMENT</h1>
    <p class="hero-text">Lorem Ipsum is simply dummy text of the printing and typesetting industry. Lorem Ipsum has beenLorem Ipsum is simply dummy text of the printing and type-setting industry. Lorem Ipsum has been</p>
    <a class="btn-more" href="#">Read More</a>
  </div>
</section>

<section class="help">
  <h2 class="help-heading">HOW COULD <span>WE HELP ?</span></h2>
  <div class="help-card" style="left:112px">
    <div class="help-photo" role="img" aria-label="Volunteer carrying folded relief blankets" style="background:linear-gradient(135deg,#b7a08c,#6f7b7e)"></div>
    <h3 class="help-title">Services</h3>
    <p class="help-text">Lorem Ipsum is simply dummy text of the printing and typesetting industry. Lorem Ipsum has been</p>
  </div>
  <div class="help-card" style="left:447px">
    <div class="help-photo" role="img" aria-label="Rescue team in orange suits searching rubble" style="background:linear-gradient(135deg,#8fa7c4,#c9773f 55%,#8a8d8e)"></div>
    <h3 class="help-title">Experience</h3>
    <p class="help-text">Lorem Ipsum is simply dummy text of the printing and typesetting industry. Lorem Ipsum has been</p>
  </div>
  <div class="help-card" style="left:788px">
    <div class="help-photo" role="img" aria-label="Person carrying a supply sack from a relief helicopter" style="background:linear-gradient(135deg,#5f7d60,#c9b7a0 55%,#d8d2c6)"></div>
    <h3 class="help-title">Turn-key Response</h3>
    <p class="help-text">Lorem Ipsum is simply dummy text of the printing and typesetting industry. Lorem Ipsum has been</p>
  </div>
</section>

<section class="band">
  <div class="band-photo" role="img" aria-label="Storm-damaged trees and utility pole"></div>
  <div class="band-panel"></div>
</section>
</body>
</html>
```